キャリア層をターゲットとしたセミナーを開催予定です。落ち着いた雰囲気のデザインをお願いします。(講演内容は添付ファイルをご確認ください)
開催団体:一般社団法人あおぞら地域交流センター
〒521-0342滋賀県米原市柏原台4-7-15
TEL:0749-38-2951
TEL:0120-394-667
A4
片面
• 高解像度JPG (.jpg)

洗練されたデザインや文字の配置、対象となるターゲットにフィットすると思い選択いたしました。
ご提案ありがとうございました。

皆さま、貴重なアイディアをくださり本当にありがとうございました。
どれか一つ選択することが大変心苦しいのですが、
今回このような結果を出させていただきました。
今後ともよろしくお願いいたします。

```html
<!DOCTYPE html>
<html lang="ja">
<head>
<meta charset="utf-8">
<title>言葉が人を動かす、自分を変える セミナー</title>
<link rel="stylesheet" href="https://fonts.googleapis.com/css2?family=Noto+Sans+JP:wght@400;500;700;900&family=Noto+Serif+JP:wght@500;700&display=swap">
<style>
:root{
  --navy:#1e2b4d;
  --orange:#e0891c;
  --ink:#3a3a3a;
  --paper:#ffffff;
  --line:#d9cbb6;
}
*{margin:0;padding:0;box-sizing:border-box}
html,body{width:851px;height:1200px;overflow:hidden;background:#fff}
.poster{position:relative;width:851px;height:1200px;background:var(--paper);font-family:"Noto Sans JP",sans-serif;color:var(--ink);overflow:hidden}
.hero-photo{position:absolute;left:0;top:0;width:851px;height:560px;
  background:
   radial-gradient(circle at 70% 18%,rgba(240,170,90,.45),transparent 22%),
   radial-gradient(circle at 88% 40%,rgba(236,160,80,.35),transparent 18%),
   radial-gradient(circle at 20% 30%,rgba(120,120,125,.55),transparent 35%),
   linear-gradient(180deg,#e9e3db 0%,#efe9e2 60%,#ffffff 100%);}
.lead{position:absolute;right:24px;top:24px;writing-mode:vertical-rl;font-family:"Noto Serif JP",serif;font-weight:700;color:#a4621a;font-size:21px;line-height:30px;letter-spacing:2px}
.headline{position:absolute;right:96px;top:60px;writing-mode:vertical-rl;font-weight:900;color:var(--navy);font-size:64px;line-height:100px;letter-spacing:0}
.headline span{display:block}
.headline .l2,.headline .l3{padding-top:50px}
.speaker-photo{position:absolute;left:700px;top:330px;width:124px;height:124px;border-radius:50%;background:linear-gradient(135deg,#3b4256,#7a7f8c 60%,#c9c4bd);border:4px solid #fff}
.date{position:absolute;left:0;width:851px;top:548px;text-align:center;color:var(--navy);font-weight:900;white-space:nowrap;line-height:90px}
.date .yr{font-size:46px}
.date .md{font-size:80px;letter-spacing:-1px}
.date .dow{display:inline-block;width:50px;height:50px;border-radius:50%;background:var(--navy);color:#fff;font-size:28px;line-height:50px;vertical-align:18px;margin-left:8px}
.time{position:absolute;left:0;width:851px;top:636px;text-align:center;color:var(--orange);font-weight:700;font-size:38px;line-height:44px}
.time small{font-size:24px}
.story{position:absolute;left:40px;top:705px;width:390px;font-size:14px;line-height:23px}
.story p{margin-bottom:12px}
.story .accent{color:var(--navy);font-weight:700;font-size:18px;line-height:27px}
.story em{font-style:normal;color:var(--orange);font-weight:700}
.course{position:absolute;left:450px;top:705px;width:365px}
.course-tag{display:inline-block;background:var(--orange);color:#fff;font-weight:700;font-size:20px;line-height:30px;padding:0 14px}
.course-tag small{font-size:12px;font-weight:500;margin-left:6px}
.course-meta{margin-top:6px;font-size:13px;border-bottom:1px solid var(--line);padding-bottom:5px}
.course-title{margin-top:8px;color:var(--navy);font-weight:900;font-size:20px;white-space:nowrap}
.curriculum{margin-top:4px;font-size:13.5px;line-height:22px}
.curriculum h3{color:var(--orange);font-size:13.5px;font-weight:700}
.curriculum li{list-style:none;padding-left:16px;position:relative}
.curriculum li::before{content:"";position:absolute;left:2px;top:7px;width:8px;height:8px;border-radius:50%;background:var(--orange)}
.home-box{position:absolute;left:450px;top:975px;width:365px;border:1.5px solid var(--orange);padding:6px 12px;font-size:12.5px;line-height:19px}
.home-box h4{display:flex;align-items:center;gap:8px;color:var(--navy);font-size:16px;font-weight:700;margin-bottom:2px}
.footer{position:absolute;left:0;bottom:0;width:851px;height:115px;border-top:2px solid var(--navy);display:flex;align-items:center;padding:0 30px;gap:22px}
.org{display:flex;align-items:center;gap:10px}
.org-mark{width:58px;height:58px;border-radius:50%;background:var(--orange);flex:none}
.org-name{font-weight:700;color:var(--navy);font-size:20px}
.org-info{font-size:11px;line-height:16px}
.apply-label{font-size:13px;color:var(--navy);font-weight:700}
.apply-tel{display:flex;align-items:center;gap:6px;color:var(--navy);font-weight:900;font-size:32px;line-height:40px;white-space:nowrap}
.hours{font-size:12px;line-height:18px}
</style>
</head>
<body>
<main class="poster">
  <div class="hero-photo" role="img" aria-label="スタンドマイクを捉えた写真、背景に暖色の光のぼかし"></div>
  <p class="lead">ハートレー元首相のスピーチに<br>隠された伝える力とは？</p>
  <h1 class="headline"><span class="l1">言葉が</span><span class="l2">人を動かす、</span><span class="l3">自分を変える</span></h1>
  <div class="speaker-photo" role="img" aria-label="演説する講演題材の人物の円形写真"></div>

  <div class="date"><span class="yr">2021年</span><span class="md">9月24日</span><span class="dow">金</span></div>
  <div class="time">19:00 - 20:00 <small>(受付18:45~)</small></div>

  <section class="story">
    <p>あがり症があり人前での会話を不安にする方へ。今回の講師は話し方を学び、緊張と上手に付き合えるようになりました。</p>
    <p>人前に立つと頭が真っ白になる、その悩みは特別なものではありません。伝える力は誰でも身につけられます。</p>
    <p class="accent">気づけば、話すことを避ける<br>クセがついていた…</p>
    <p>そんな経験を変えるきっかけとして、<em>言葉が持つ大きな力</em>を一緒に学んでみませんか。話す自信は、自分を変える第一歩です。</p>
  </section>

  <section class="course">
    <span class="course-tag">オンライン60分講座<small>無料</small></span>
    <p class="course-meta">講師：ひだまり話し方認定講師　定員：10名(受講無料)</p>
    <h2 class="course-title">どうして人前であがってしまうのか</h2>
    <div class="curriculum">
      <h3>カリキュラム</h3>
      <ul>
        <li>講師の自己紹介と話し方との出会い</li>
        <li>あがり症を感じる原因について</li>
        <li>緊張を味方にする考え方</li>
        <li>伝わる話し方の基本ポイント</li>
        <li>毎日できる簡単トレーニング</li>
        <li>質疑応答とこれからの学び方</li>
      </ul>
    </div>
  </section>

  <aside class="home-box">
    <h4><svg width="24" height="18" viewBox="0 0 24 18"><rect x="3" y="1" width="18" height="12" rx="1" fill="none" stroke="#1e2b4d" stroke-width="2"/><rect x="0" y="14" width="24" height="3" fill="#1e2b4d"/></svg>自宅で学べるオンライン講座</h4>
    <p>お申込み後に参加用のURLをお送りします。パソコンやスマートフォンから気軽にご参加いただけます。</p>
  </aside>

  <footer class="footer">
    <div class="org">
      <div class="org-mark"></div>
      <div>
        <div class="org-info">主催：一般社団法人あおぞら地域交流センター</div>
        <div class="org-name">あおぞら</div>
        <div class="org-info">〒521-0342滋賀県米原市柏原台4-7-15<br>TEL:0749-38-2951</div>
      </div>
    </div>
    <div class="apply">
      <div class="apply-label">受講お申し込み</div>
      <div class="apply-tel"><svg width="28" height="28" viewBox="0 0 24 24"><path fill="#1e2b4d" d="M6.6 10.8a15 15 0 0 0 6.6 6.6l2.2-2.2a1 1 0 0 1 1-.25 11.4 11.4 0 0 0 3.6.57 1 1 0 0 1 1 1V20a1 1 0 0 1-1 1A17 17 0 0 1 3 4a1 1 0 0 1 1-1h3.5a1 1 0 0 1 1 1c0 1.25.2 2.45.57 3.57a1 1 0 0 1-.25 1z"/></svg>0120-394-667</div>
    </div>
    <div class="hours">受付時間/平日10:00~17:00<br>https://aozora-koryu.jp</div>
  </footer>
</main>
</body>
</html>
```